Business card needed for the Vantro of Dry Cleaning!

We need a slick business card design for a new company based out of Montreal called Casiers Pli&Zip inc. (in French) and Pli&Zip Lockers inc. (in English). We're the Vantro of Laundry. We offer services of dry cleaning, laundry (wash&fold), minor clothing alterations, shoe repair and parcel delivery through 24/7 secured and connected lockers. Ordres are placed through our mobile application. Real time notification are sent to customers when their order is ready for pickup. The lockers will be placed throughout the downtown area, in condo and office towers, where a high density of busy people converge. It is simple, user-friendly, and most importantly convenient. We're the out of the box dry cleaner, literally.
Updates

Target Market(s)

1) Professional workers wearing suits daily
2) Campus students living in residences
3) People using laundromats
4) Families with children/yuppies who prefer to use their time doing something else than laundry

Industry/Entity Type

Dry Cleaning

Contact Information for Business Card

Name / Sylvie-Anne Berthiaume
Title / CEO & Founder
Company Name / Casiers Pli&Zip inc. | Pli&Zip Lockers inc.
Website www.plizip.ca

Requirements
Must have
• Text Logo: Pli&Zip - Nettoyeurs 24/7 Cleaners
• Logo on one side and contact info on the other (bilingual)
• Minimalist, pure design
• "We care" for your belongings feeling
• Professional, technological, clean & fresh look
Should not have
• No busy visuals. No rainbow colors.

```html
<!DOCTYPE html>
<html lang="fr">
<head>
<meta charset="utf-8">
<title>Pli&amp;Zip – Business Card</title>
<link rel="stylesheet" href="https://fonts.googleapis.com/css2?family=Open+Sans:wght@400;600;700&display=swap">
<style>
  :root {
    --backdrop: #2f5366;
    --brand-blue: #0a86d1;
    --brand-blue-deep: #0a7fcc;
    --paper: #ffffff;
    --ink-grey: #8a8a8a;
  }
  * { margin: 0; padding: 0; box-sizing: border-box; }
  html, body {
    width: 1200px; height: 1000px; overflow: hidden;
    background: var(--backdrop);
    font-family: "Open Sans", Arial, sans-serif;
  }
  .stage { position: relative; width: 1200px; height: 1000px; }

  .card {
    position: absolute;
    width: 607px; height: 355px;
  }
  .card--front { left: 108px; top: 189px; background: var(--paper); z-index: 2; }
  .card--back  { left: 487px; top: 498px; background: var(--brand-blue); z-index: 1; }

  .brand {
    position: absolute;
    display: flex; align-items: center;
    font-weight: 700;
    white-space: nowrap;
  }
  .brand__mark { flex: none; border-radius: 0; }
  .card--front .brand { left: 34px; top: 41px; gap: 16px; color: var(--brand-blue-deep); font-size: 40px; }
  .card--front .brand__mark { width: 58px; height: 58px; background: var(--brand-blue-deep); }
  .card--back .brand { left: 50%; top: 50%; transform: translate(-50%, -50%); gap: 22px; color: var(--paper); font-size: 54px; }
  .card--back .brand__mark { width: 82px; height: 82px; background: var(--paper); }

  .person__name {
    position: absolute; left: 34px; top: 146px;
    font-size: 24px; font-weight: 600; color: var(--brand-blue-deep);
    white-space: nowrap;
  }
  .person__title {
    position: absolute; left: 0; top: 182px; width: 100%; height: 26px;
    background: var(--brand-blue);
    color: var(--paper); font-size: 16px; line-height: 26px;
    padding-left: 33px;
  }
  .contact {
    position: absolute; left: 34px; top: 244px;
    list-style: none;
    font-size: 16px; line-height: 20px; color: var(--ink-grey);
    white-space: nowrap;
  }
  .contact__label { color: var(--brand-blue-deep); font-weight: 600; }
</style>
</head>
<body>
<main class="stage">
  <section class="card card--back" aria-label="Verso – logo">
    <div class="brand">
      <span class="brand__mark"></span>
      <span class="brand__name">Pli&amp;Zip</span>
    </div>
  </section>

  <section class="card card--front" aria-label="Recto – coordonnées">
    <div class="brand">
      <span class="brand__mark"></span>
      <span class="brand__name">Pli&amp;Zip</span>
    </div>
    <h1 class="person__name">Sylvie-Anne Berthiaume</h1>
    <p class="person__title">CEO &amp; Founder</p>
    <ul class="contact">
      <li><span class="contact__label">T:</span> 123-4567-890</li>
      <li><span class="contact__label">E:</span> info@plizip.ca</li>
      <li><span class="contact__label">W:</span> www.plizip.ca</li>
      <li><span class="contact__label">A:</span> Office No.123, ABC Building, 1st Floor, City, Country.</li>
    </ul>
  </section>
</main>
</body>
</html>
```